Radiant Crossing - An Exciting Mission & Book Cover Project

Help me to inspire people to live their best life! This is a mission, not just a design project.
I need a Book Cover designed to keep me inspired on the process of writing my book.
Book Title: Radiant Crossing
Tag Line: Three Simple Steps to get out of your own way, SuperCharge your Life and Step into Purpose!
Author: Marlis Quenby

The three steps are: Ownership, Vision and Action (Not sure if this should be on the front or back of the book cover)

The book is a self-help, motivational book. Personal development.
The cover needs to be strong and capture peoples attention, especially with competing shelf space. I almost see a fire ball of flame or explosion that will grab peoples attention.
My company is The Lantern Institute. I have added the company logo and a few pages of my presentation and topic outline to give an idea.
Maybe: The Lantern Institute logo on back of the cover. website is marlisquenby.com

THOUGHT: People should be able to take a photo of them holding the book cover showing what area of life they want Radiant Crossing in. This is why the front cover must be so visual and powerful that they want to take a photo with it. Ie. Explosion, fire, strong and bold.

Target Market(s)

Anyone who feels stuck and needs to breakthrough and move forward in life.

Industry/Entity Type

Motivation

Font styles to use
Serif
Sans Serif

Colors
ec1f27
f37122
fbed22

Requirements
Must have
• The design must be STRONG, SIMPLE, STAND OUT ON BOOK SHELVES.
Must have an open file to swap the photo and copy out.

Back Cover Page
1) Summary
2) 2-3 testimonials. One sentence.
3) About the Author (maybe with photo)
4) Lantern Institute logo
5) Website: radiantcrossing.com and marlisquenby.com
Nice to have
• If my photo works somewhere that would be great. I will change the photo later.
Added Where's Your Harbor? a nice cover example.
Should not have
• Right now I am writing the summary for the back of the cover. For now use Loreum Ipsum text and 2-3 recommendations. Again, I will get these only later.

```html
<!DOCTYPE html>
<html lang="en">
<head>
<meta charset="utf-8">
<title>Radiant Crossing – Book Cover</title>
<link rel="stylesheet" href="https://fonts.googleapis.com/css2?family=Montserrat:wght@300;900&family=Roboto:wght@400;500&family=Roboto+Condensed:wght@700&family=Tinos&display=swap">
<style>
  :root {
    --canvas: #e6e7e8;
    --cover: #141414;
    --spine: #f7ec22;
    --orange: #f37122;
    --red: #ec1f27;
    --yellow: #fbed22;
    --white: #ffffff;
    --ink: #111111;
  }
  * { margin: 0; padding: 0; box-sizing: border-box; }
  html, body { width: 1200px; height: 1000px; overflow: hidden; background: var(--canvas); }
  .canvas { position: relative; width: 1200px; height: 1000px; }

  .cover { position: absolute; left: 14px; top: 93px; width: 1172px; height: 814px; background: var(--cover); display: flex; }
  .panel { position: relative; height: 100%; overflow: hidden; }
  .front { width: 542px; }
  .spine { width: 90px; background: var(--spine); }
  .back { width: 540px; }

  .gradient-text {
    background: linear-gradient(90deg, var(--orange) 0%, #f9b31d 55%, var(--yellow) 100%);
    -webkit-background-clip: text; background-clip: text; color: transparent;
  }
  .title { position: absolute; z-index: 2; left: 0; width: 100%; text-align: center; font-family: "Montserrat", sans-serif; font-weight: 900; line-height: 1; text-transform: uppercase; }
  .title span { display: block; }
  .title-main { font-size: 78px; letter-spacing: 6px; }
  .title-sub { font-size: 57px; letter-spacing: 2px; margin-top: 6px; }

  .front .title { top: 26px; }
  .burst {
    position: absolute; z-index: 1; left: 16px; top: 150px; width: 516px; height: 456px;
    border-radius: 50%;
    background: radial-gradient(ellipse at 48% 45%, #fde26a 0%, #f9a21f 28%, var(--orange) 52%, #d8431d 66%, rgba(236,31,39,0.35) 74%, rgba(20,20,20,0) 82%);
  }
  .tagline { position: absolute; z-index: 2; top: 622px; left: 0; width: 100%; text-align: center; color: var(--white); font-family: "Montserrat", sans-serif; font-weight: 300; font-size: 19px; line-height: 23px; }
  .front-author { position: absolute; z-index: 2; top: 748px; left: 0; width: 100%; text-align: center; font-family: "Montserrat", sans-serif; font-weight: 900; font-size: 36px; letter-spacing: 1px; }

  .spine-text { position: absolute; left: 45px; transform-origin: 0 0; transform: rotate(90deg); white-space: nowrap; font-family: "Roboto Condensed", sans-serif; font-weight: 700; font-size: 36px; color: var(--ink); text-transform: uppercase; translate: 18px 0; }
  .spine-title { top: 47px; }
  .spine-author { top: 555px; }

  .back .title { top: 26px; }
  .summary { position: absolute; top: 208px; left: 40px; width: 460px; text-align: center; font-family: "Tinos", serif; font-size: 18.5px; line-height: 26px; color: var(--white); text-transform: uppercase; }
  .summary p + p { margin-top: 26px; }
  .author-photo { position: absolute; left: 42px; top: 484px; width: 134px; height: 116px; border: 1.5px solid #d8d8d8; }
  .about { position: absolute; left: 194px; top: 492px; font-family: "Roboto", sans-serif; }
  .about-name { color: var(--yellow); font-size: 28px; font-weight: 400; text-transform: uppercase; }
  .about-bio { color: var(--white); font-size: 19px; line-height: 26px; margin-top: 16px; }
  .imprint { position: absolute; left: 40px; top: 686px; width: 172px; text-align: center; font-family: "Roboto", sans-serif; font-weight: 500; color: var(--white); font-size: 13px; letter-spacing: 0.5px; text-transform: uppercase; }
  .imprint-mark { display: block; width: 34px; height: 34px; margin: 0 auto 20px; border-radius: 50%; background: var(--orange); }
</style>
</head>
<body>
<div class="canvas">
  <div class="cover">
    <section class="panel front">
      <h1 class="title gradient-text"><span class="title-main">Radiant</span><span class="title-sub">Crossing</span></h1>
      <div class="burst" role="img" aria-label="Fiery explosion burst with red spikes, lightning and halftone dots"></div>
      <p class="tagline">“ Three Simple Steps to get<br>out of your own way, SuperCharge your<br>Lifeand Step into Purpose ”</p>
      <p class="front-author gradient-text">MARLIS QUENBY</p>
    </section>

    <section class="panel spine">
      <span class="spine-text spine-title">Radiant Crossing</span>
      <span class="spine-text spine-author">Marlis Quenby</span>
    </section>

    <section class="panel back">
      <h2 class="title gradient-text"><span class="title-main">Radiant</span><span class="title-sub">Crossing</span></h2>
      <div class="summary">
        <p>Lorem Ipsum is simply dummy text of<br>the printing and typesetting<br>industry. Lorem Ipsum has been the</p>
        <p>Lorem Ipsum is simply dummy text of<br>the printing and typesetting<br>industry. Lorem Ipsum has been the<br>industry's standard dummy</p>
      </div>
      <div class="author-photo"></div>
      <div class="about">
        <p class="about-name">Marlis Quenby</p>
        <p class="about-bio">Lorem Ipsum is simply<br>dummy text of the printing and</p>
      </div>
      <div class="imprint"><span class="imprint-mark"></span>The Lantern Institute</div>
    </section>
  </div>
</div>
</body>
</html>
```